Commercial Bakery needs packing design for a Bread Bag.

Dorne's Bakery needs a design for a bread bag to be distributed to grocery stores. We make all kinds of breads and want this packaging to represent our company. We would like the packaging to be black and white with a fun/bubbly modern design. I have attached a few ideas of what I am looking for.
There are 5 different products. Packaging must be the same for each product except for corresponding product name, bar code and nutrional facts.
Product names:
Coconut Cream Bread
Cream Bread
Potato Rolls
Roll ups
Coconut & Raisin Bread

Our products are packaged in a 11” x 8” poly bag.
I will open 5 contracts with whoever’s design I select. I will then provide nutritional facts, barcodes for items once a contract is selected. Thank you!!

Target Market(s)

Grocery stores

Industry/Entity Type

Bakery

Requirements
Must have
• Black and White (off whites are ok)
Should not have
• Color

```html
<!DOCTYPE html>
<html lang="en">
<head>
<meta charset="utf-8">
<title>Dorne's Bakery – Coconut Cream Bread Bag</title>
<link href="https://fonts.googleapis.com/css2?family=Bebas+Neue&display=swap" rel="stylesheet">
<style>
  :root {
    --backdrop: #6f6e6f;
    --ink: #1c1c1c;
    --ink-soft: #3a3a3a;
    --paper: #f4f3f1;
    --crust-light: #f1dcc0;
    --crust-mid: #e2b47e;
    --crust-dark: #c98a4e;
  }
  html, body {
    margin: 0;
    padding: 0;
    width: 1174px;
    height: 1200px;
    overflow: hidden;
    background: var(--backdrop);
  }
  .canvas {
    position: relative;
    width: 1174px;
    height: 1200px;
  }
  .bag-front {
    position: absolute;
    left: 377px;
    top: 410px;
    width: 338px;
    height: 644px;
    background: var(--paper);
    overflow: hidden;
  }
  .bread-window {
    position: absolute;
    left: 0;
    top: 0;
    width: 338px;
    height: 306px;
    background: linear-gradient(90deg, var(--crust-dark) 0%, var(--crust-mid) 12%, var(--crust-light) 45%, var(--crust-light) 70%, var(--crust-mid) 92%, var(--crust-dark) 100%);
  }
  .label-edge {
    position: absolute;
    left: 0;
    top: 293px;
    width: 338px;
    height: 8px;
  }
  .label-edge svg { display: block; }
  .brand-mark {
    position: absolute;
    left: 103px;
    top: 231px;
    width: 148px;
    height: 148px;
    border-radius: 50%;
    background: var(--paper);
    border: 2px solid var(--ink);
    box-sizing: border-box;
    display: flex;
    align-items: center;
    justify-content: center;
  }
  .brand-name {
    font-family: "Bebas Neue", sans-serif;
    color: var(--ink);
    font-size: 32px;
    line-height: 0.95;
    text-align: center;
    letter-spacing: 1px;
  }
  .product-name {
    position: absolute;
    left: 0;
    top: 400px;
    width: 338px;
    margin: 0;
    font-family: "Bebas Neue", sans-serif;
    font-weight: 400;
    color: var(--ink);
    font-size: 47px;
    line-height: 41px;
    text-align: center;
    letter-spacing: 0.5px;
  }
  .wheat-band {
    position: absolute;
    left: 0;
    top: 506px;
    width: 338px;
    height: 138px;
    background:
      radial-gradient(circle at 12% 30%, var(--ink-soft) 0, transparent 22%),
      radial-gradient(circle at 38% 70%, var(--ink-soft) 0, transparent 20%),
      radial-gradient(circle at 62% 25%, var(--ink-soft) 0, transparent 22%),
      radial-gradient(circle at 88% 65%, var(--ink-soft) 0, transparent 22%),
      radial-gradient(circle at 25% 95%, var(--ink-soft) 0, transparent 16%),
      radial-gradient(circle at 78% 5%, var(--ink-soft) 0, transparent 16%),
      var(--ink);
  }
  .net-weight {
    position: absolute;
    left: 121px;
    bottom: 0;
    width: 100px;
    height: 21px;
    background: var(--paper);
    border-radius: 3px 3px 0 0;
    font-family: "Bebas Neue", sans-serif;
    font-size: 16px;
    line-height: 23px;
    text-align: center;
    color: var(--ink);
  }
</style>
</head>
<body>
<div class="canvas">
  <div class="bag-front">
    <div class="bread-window" role="img" aria-label="Photo of sliced white bread loaf seen through the clear bag"></div>

    <div class="label-edge">
      <svg width="338" height="8" viewBox="0 0 338 8" aria-hidden="true">
        <defs>
          <pattern id="zigzag" width="6" height="8" patternUnits="userSpaceOnUse">
            <polygon points="0,8 3,0 6,8" fill="#f4f3f1"/>
          </pattern>
        </defs>
        <rect width="338" height="8" fill="url(#zigzag)"/>
      </svg>
    </div>

    <div class="brand-mark">
      <div class="brand-name">Dorne's<br>Bakery</div>
    </div>

    <h1 class="product-name">Coconut Cream<br>Bread</h1>

    <div class="wheat-band" role="img" aria-label="Decorative pattern of white wheat stalks and grains on black">
      <div class="net-weight">Net Wet. 16oz</div>
    </div>
  </div>
</div>
</body>
</html>
```